The K7 Momentum Collective Website

We have a pitch deck and messaging drafted. Target audience is academic institutions and VC investors that have seed money in start ups.

Need a basic website

Industry/Entity Type

LIfe Science, Diagnostic, medical device.

Coding

Coded - Design and coding required

Number of Pages Required

5+ page

```html
<!DOCTYPE html>
<html lang="en">
<head>
<meta charset="utf-8">
<title>The K7 Momentum Collective</title>
<link href="https://fonts.googleapis.com/css2?family=Nunito:wght@400;600;700;800;900&family=Nunito+Sans:wght@400;600;700&display=swap" rel="stylesheet">
<style>
:root{
  --teal:#4dbdb9;
  --teal-soft:#7fd3cf;
  --teal-pale:#d3f1f2;
  --teal-dark:#1e7a78;
  --teal-deep:#1a6f6d;
  --ink:#2b2f33;
  --muted:#5a6166;
  --link:#3aa7b0;
  --white:#ffffff;
  --page:#ffffff;
}
*{box-sizing:border-box;margin:0;padding:0}
html,body{width:1200px;height:4912px;overflow:hidden;background:var(--page)}
body{font-family:"Nunito Sans",Arial,sans-serif;color:var(--ink);position:relative}
.abs{position:absolute}
h1,h2,h3{font-family:"Nunito",Arial,sans-serif}

/* nav + hero */
.hero{left:0;top:0;width:1200px;height:900px;background:var(--teal)}
.hero-wave{left:0;top:560px;width:1200px;height:360px}
.nav{left:0;top:0;width:1200px;height:109px;border-bottom:1px solid rgba(255,255,255,.45);display:flex;justify-content:center;align-items:center;gap:54px}
.nav a{color:var(--white);font-size:15px;text-decoration:none;font-weight:600}
.hero-title{left:98px;top:195px;color:var(--white);font-size:70px;line-height:70px;font-weight:900;letter-spacing:.5px}
.hero-tag{left:98px;top:478px;color:var(--white);font-size:21px}
.btn-hero{left:98px;top:538px;width:168px;height:48px;background:var(--teal-dark);color:var(--white);font-size:15px;display:flex;align-items:center;padding-left:22px;gap:26px}
.hero-art{left:560px;top:140px;width:510px;height:540px;border-radius:24px;background:radial-gradient(circle at 50% 50%,#eaf6f6 0%,#b8e3e1 45%,rgba(77,189,185,0) 72%)}

/* intro */
.intro-photo{left:98px;top:889px;width:502px;height:408px;border:4px solid var(--teal);border-radius:26px;background:linear-gradient(135deg,#e9eceb 0%,#cfd3d2 45%,#d8322f 46%,#e23b36 70%,#d9dcdb 71%)}
.sec-head{color:var(--teal-dark);font-size:38px;font-weight:700}
.intro-head{left:638px;top:900px}
.intro-text{left:638px;top:972px;width:460px;font-size:15px;line-height:21px;color:var(--ink)}
.intro-text p{margin-bottom:21px}
.intro-text em{font-style:normal;color:var(--link)}

/* problem */
.problem-bg{left:0;top:1240px;width:1200px;height:900px}
.problem-head{left:98px;top:1462px}
.problem-text{left:98px;top:1540px;width:500px;font-size:14.5px;line-height:20px}
.problem-text p{margin-bottom:22px}
.problem-text strong{display:block;font-weight:700}
.ticks{list-style:none;margin-bottom:24px}
.ticks li{position:relative;padding-left:26px}
.ticks li::before{content:"";position:absolute;left:0;top:3px;width:15px;height:15px;border-radius:50%;background:var(--teal)}
.ticks li::after{content:"";position:absolute;left:4px;top:6px;width:6px;height:4px;border-left:2px solid #fff;border-bottom:2px solid #fff;transform:rotate(-45deg)}
.problem-art{left:653px;top:1466px;width:457px;height:464px;border-radius:24px;background:linear-gradient(180deg,rgba(255,255,255,0) 0%,#b9d4ec 45%,#4f7fc2 100%)}

/* team */
.team-head{left:0;top:2112px;width:1200px;text-align:center}
.rule{height:4px;width:50px;background:var(--teal)}
.team-rule{left:575px;top:2178px}
.card{top:2300px;width:297px;height:455px;background:var(--white);border-radius:14px;box-shadow:0 6px 26px rgba(0,0,0,.12);text-align:center;padding:90px 22px 0}
.avatar{top:2222px;width:128px;height:128px;border-radius:50%;border:4px solid #fff;box-shadow:0 4px 14px rgba(0,0,0,.15);background:linear-gradient(180deg,#cfd8dc,#8f9ba1)}
.card h3{color:var(--teal-dark);font-size:26px;font-weight:800}
.card .role{color:var(--teal-dark);font-size:14px;font-weight:700;margin:6px 0 20px}
.card p{font-size:12.5px;line-height:17px;color:var(--muted);margin-bottom:18px}
.card .contact{color:var(--teal-dark);font-weight:700;font-size:12.5px;line-height:17px}

/* discovery */
.disc-head{left:98px;top:2828px}
.disc-rule{left:98px;top:2898px}
.disc-steps{left:98px;top:2921px;width:502px;height:204px;display:flex}
.step{flex:1;color:#fff;display:flex;flex-direction:column;align-items:center;justify-content:flex-end;padding-bottom:22px;font-size:14px;line-height:17px;text-align:center;gap:30px}
.step svg{width:56px;height:56px}
.s1{background:var(--teal-dark)}.s2{background:var(--teal)}.s3{background:var(--teal-deep)}.s4{background:#5cc3bf}
.assess-head{left:638px;top:2828px}
.assess-rule{left:638px;top:2898px}
.assess-text{left:638px;top:2935px;width:460px;font-size:14px;line-height:20px}
.assess-text p{margin-bottom:20px}

/* voc */
.voc{left:0;top:3206px;width:1200px;height:372px;background:var(--teal-dark)}
.voc-head{left:0;top:3250px;width:1200px;text-align:center;color:#fff;font-size:38px;font-weight:600}
.voc-rule{left:575px;top:3312px;background:#fff}
.voc-row{left:98px;top:3350px;width:1000px;display:flex;gap:20px}
.voc-item{flex:1;display:flex;align-items:flex-start;gap:12px;border-bottom:1px solid rgba(255,255,255,.7);padding-bottom:8px;height:96px}
.voc-num{font-family:"Nunito",sans-serif;font-size:96px;line-height:86px;font-weight:300;color:transparent;-webkit-text-stroke:2px #fff}
.voc-label{color:#fff;font-size:14.5px;line-height:18px;padding-top:6px}
.btn-voc{left:517px;top:3496px;width:166px;height:50px;background:#fff;color:var(--teal-dark);font-size:14px;display:flex;align-items:center;justify-content:center;gap:22px}

/* plan */
.plan-head{left:98px;top:3630px}
.plan-rule{left:98px;top:3698px}
.plan-list{left:98px;top:3722px;width:1000px;font-size:14px;line-height:19.5px}
.plan-list li{margin-bottom:4px}
.plan-list b{color:var(--teal-dark)}

/* contact */
.foot-bg{left:0;top:4440px;width:1200px;height:472px}
.contact-card{left:98px;top:4123px;width:1000px;height:475px;background:#fff;box-shadow:0 8px 30px rgba(0,0,0,.14);border-radius:8px;overflow:hidden}
.form{left:30px;top:30px;width:484px}
.form h2{color:var(--teal-dark);font-size:32px;font-weight:600;margin-bottom:30px}
.fields{display:grid;grid-template-columns:1fr 1fr;gap:12px 24px}
.field{height:40px;border:1px solid #cfd6d8;font-size:11px;color:#8a9397;padding:12px 10px}
.field.wide{grid-column:1 / 3;height:118px}
.send{margin-top:12px;height:42px;background:var(--teal-dark);color:#fff;font-size:11px;font-weight:700;letter-spacing:1px;display:flex;align-items:center;justify-content:center}
.details{left:544px;top:0;width:456px;height:475px;background:var(--teal-dark);padding:30px 28px;color:#fff}
.details h2{font-size:32px;font-weight:600;margin-bottom:34px}
.d-row{display:flex;align-items:center;gap:16px;font-size:14px;line-height:19px;padding-bottom:20px;margin-bottom:20px;border-bottom:1px solid rgba(255,255,255,.35)}
.d-row svg{width:30px;height:30px;flex:none}
.d-row.big{font-size:20px}
.socials{display:flex;gap:26px;font-size:14px}
.socials span{display:flex;align-items:center;gap:8px}
.socials i{width:24px;height:24px;border-radius:50%;background:#fff;display:inline-block}

.foot-title{left:98px;top:4660px;color:#fff;font-size:48px;line-height:50px;font-weight:900}
.foot-links{left:695px;top:4690px;width:420px;color:#fff;font-size:13.5px;line-height:20px}
.foot-links p{margin-bottom:16px}
.foot-links b{font-weight:700}
.foot-line{left:0;top:4842px;width:1200px;border-top:1px solid rgba(255,255,255,.45)}
.copy{left:0;top:4864px;width:1200px;text-align:center;color:#fff;font-size:12px;letter-spacing:.3px}
</style>
</head>
<body>

<!-- hero -->
<div class="abs hero"></div>
<svg class="abs hero-wave" viewBox="0 0 1200 360" preserveAspectRatio="none">
  <path d="M0 220 C180 120 320 150 520 170 C760 195 900 110 1200 70 L1200 360 L0 360Z" fill="#7fd3cf"/>
  <path d="M0 290 C200 200 380 250 580 260 C800 270 960 170 1200 140 L1200 360 L0 360Z" fill="#a8e1de"/>
  <path d="M0 330 C220 250 420 310 640 300 C860 290 1010 220 1200 200 L1200 360 L0 360Z" fill="#ffffff"/>
</svg>
<nav class="abs nav">
  <a>Home</a><a>Our Solutions</a><a>Voice of Customer (VOC)</a><a>K7 Plan Elements</a><a>Contact Us</a>
</nav>
<h1 class="abs hero-title">The K7<br>Momentum<br>Collective™</h1>
<p class="abs hero-tag">Accelerating your innovative IP to market!</p>
<div class="abs btn-hero">Contact Us
  <svg width="30" height="12" viewBox="0 0 30 12"><path d="M0 6H26M21 1L27 6L21 11" stroke="#fff" stroke-width="1.4" fill="none"/></svg>
</div>
<div class="abs hero-art" role="img" aria-label="Illustration of business people turning a large set of gears labelled resources, strategy, planning and control"></div>

<!-- intro -->
<div class="abs intro-photo" role="img" aria-label="Photo of grey jigsaw puzzle with a red missing piece"></div>
<h2 class="abs sec-head intro-head">Introduction</h2>
<div class="abs intro-text">
  <p>The K7 Momentum Collective (K7) rapidly brings innovative and transformational IP to market by assisting with all elements of a company's development.</p>
  <p><em>We Are...</em>experienced in strategic business planning and execution, and operational excellence.</p>
  <p><em>We Have...</em>100 years of collective experiences and vast network of people, partners, and processes.</p>
  <p><em>We Can...</em>serve as the initial executive team to ensure strategic alignment with a focus on marketplace.</p>
  <p><em>We Will...</em>remove the uncertainty and confusion common in the initial stages of a company's formation.</p>
</div>

<!-- problem -->
<svg class="abs problem-bg" viewBox="0 0 1200 900" preserveAspectRatio="none">
  <path d="M0 170 C160 140 300 150 460 160 C700 175 860 60 1200 10 L1200 640 C1000 660 880 600 720 640 C560 690 420 860 220 820 C110 800 40 760 0 740Z" fill="#d3f1f2"/>
  <path d="M0 740 C60 780 140 820 240 830 C420 850 560 690 720 650" stroke="#4dbdb9" stroke-width="3" fill="none"/>
</svg>
<h2 class="abs sec-head problem-head">The Problem &gt; The Solution</h2>
<div class="abs problem-text">
  <p>K7 was started to solve significant problems associated with rapidly bringing innovative and transformational IP to market.</p>
  <strong>These costly problems include:</strong>
  <ul class="ticks">
    <li>Incomplete strategic planning,</li>
    <li>Difficulty finding leadership,</li>
    <li>Not able to differentiate a product or service from others that are already available, and Ignoring the needs of customer.</li>
    <li>(Capital shortages, poor locations, and scaling too soon can also cause a start-up to have problems.)</li>
  </ul>
  <p>The K7 Plan is unique to your organizational needs and secures the right people, partners, and processes to ensure an efficient start-up with strategic growth, and access to funding sources to help scale the business.</p>
</div>
<div class="abs problem-art" role="img" aria-label="Illustration of a team working on blue puzzle pieces with a lightbulb and tools"></div>

<!-- team -->
<h2 class="abs sec-head team-head">Meet The Team</h2>
<div class="abs rule team-rule"></div>

<div class="abs card" style="left:98px">
  <h3>Dana Whitfield</h3><div class="role">Partner</div>
  <p>Marketing, Commercial Development, Product Development, Growth Strategy</p>
  <p>30+ years of marketing, sales, product development, and operations executive leader in the life science and diagnostic industries.</p>
  <div class="contact">(555) 014-2281<br>dana@k7mc.example<br>k7mc.example/team/<br>dana-whitfield</div>
</div>
<div class="abs card" style="left:451px">
  <h3>Mira Castellan</h3><div class="role">Partner</div>
  <p>Regulatory, Quality, Product Development, Operations</p>
  <p>30+ years working in diagnostic and medical device area with focus on creative solutions to bring product to market.</p>
  <div class="contact">(555) 013-7740<br>mira@k7mc.example<br>k7mc.example/team/<br>mira-castellan</div>
</div>
<div class="abs card" style="left:803px">
  <h3>Owen Ratcliffe</h3><div class="role">Partner</div>
  <p>Board Development, Funding, Back-office Set-up, Operations</p>
  <p>30+ years accomplished CEO and well-rounded executive with more than 25 years of experience in medical devices, research tools and diagnostics.</p>
  <div class="contact">(555) 019-3326<br>owen@k7mc.example<br>k7mc.example/team/<br>owen-ratcliffe</div>
</div>
<div class="abs avatar" style="left:182px" role="img" aria-label="Headshot of team partner"></div>
<div class="abs avatar" style="left:535px" role="img" aria-label="Headshot of team partner"></div>
<div class="abs avatar" style="left:887px" role="img" aria-label="Headshot of team partner"></div>

<!-- discovery -->
<h2 class="abs sec-head disc-head">Discovery to Market</h2>
<div class="abs rule disc-rule"></div>
<div class="abs disc-steps">
  <div class="step s1">
    <svg viewBox="0 0 56 56"><circle cx="28" cy="28" r="12" fill="none" stroke="#fff" stroke-width="3"/><circle cx="28" cy="28" r="4" fill="#fff"/><path d="M28 8V14M28 42V48M8 28H14M42 28H48M14 14L18 18M38 38L42 42M42 14L38 18M14 42L18 38" stroke="#fff" stroke-width="3"/></svg>
    <span>Discovery</span>
  </div>
  <div class="step s2">
    <svg viewBox="0 0 56 56"><path d="M28 10C19 10 14 17 14 23C14 30 21 33 21 40H35C35 33 42 30 42 23C42 17 37 10 28 10Z" fill="none" stroke="#fff" stroke-width="3"/><path d="M22 45H34M24 50H32" stroke="#fff" stroke-width="3"/></svg>
    <span>Innovative IP</span>
  </div>
  <div class="step s3">
    <svg viewBox="0 0 56 56"><rect x="8" y="10" width="40" height="28" fill="none" stroke="#fff" stroke-width="3"/><path d="M14 32L22 24L29 29L40 17M20 38L16 48M36 38L40 48" stroke="#fff" stroke-width="3" fill="none"/></svg>
    <span>Strategic<br>Business Plan</span>
  </div>
  <div class="step s4">
    <svg viewBox="0 0 56 56"><rect x="12" y="8" width="32" height="40" rx="2" fill="none" stroke="#fff" stroke-width="3"/><path d="M19 20L23 24L31 16M19 32H37M19 39H33" stroke="#fff" stroke-width="3" fill="none"/></svg>
    <span>Company<br>Formation</span>
  </div>
</div>

<h2 class="abs sec-head assess-head">Invention Assessment</h2>
<div class="abs rule assess-rule"></div>
<div class="abs assess-text">
  <p>Review the invention disclosure &amp; provisional patent</p>
  <p><strong>Interview the inventor:</strong><br>How did the invention come about?<br>What problem were they trying to solve?<br>How complete of a solution do they think they have invented?<br>Who do they see is their biggest competitor?</p>
  <p>Brief review of the competitive landscape</p>
</div>

<!-- voc -->
<div class="abs voc"></div>
<h2 class="abs voc-head">Voice of Customer (VOC) &amp; Product Definition</h2>
<div class="abs rule voc-rule"></div>
<div class="abs voc-row">
  <div class="voc-item"><span class="voc-num">1</span><span class="voc-label">The Market<br>Case:<br>(30 - 45 days)</span></div>
  <div class="voc-item"><span class="voc-num">2</span><span class="voc-label">The Winning<br>Product:<br>(30 – 45 days)</span></div>
  <div class="voc-item"><span class="voc-num">3</span><span class="voc-label">The Product<br>Blueprint:<br>(30 – 45 days)</span></div>
  <div class="voc-item"><span class="voc-num">4</span><span class="voc-label">VOC<br>Report-out<br>(10 days)</span></div>
</div>
<div class="abs btn-voc">Read More
  <svg width="30" height="12" viewBox="0 0 30 12"><path d="M0 6H26M21 1L27 6L21 11" stroke="#1e7a78" stroke-width="1.4" fill="none"/></svg>
</div>

<!-- plan -->
<h2 class="abs sec-head plan-head">K7 Plan Elements</h2>
<div class="abs rule plan-rule"></div>
<ul class="abs ticks plan-list">
  <li><b>Executive Summary:</b> Articulates a brief snapshot of the business model/plan, including name, location, products or services, mission statement, and organizational values/ cultural beliefs.</li>
  <li><b>Company Description:</b> Describes a high-level view of the business nature, customer need being met, history, legality, short term, and long-term goals.</li>
  <li><b>Products/Services:</b> Provides a description of the product/services, its competitive advantages, customer benefits, reimbursement, estimated supplier costs, the net revenue from the sale of the product or service and after sale support.</li>
  <li><b>Market Analysis:</b> Displays research and plan to reach the target demographic as well as the size, direction, and competitors in the overall industry.</li>
  <li><b>Operations/Strategy:</b> Explains how the company will function given the sales and marketing strategy, and the plan of operations from acquisition of suppliers to delivery, including regulatory and quality plan.</li>
  <li><b>Financials:</b> Details estimates of all the important, financial documents, including balance sheet, cash flow, statement, capital, expenditure, budget, and income statement.</li>
  <li><b>Organization &amp; Management Team:</b> Shows the company structure as well as identifying divisions and key management personnel.</li>
</ul>

<!-- footer background -->
<svg class="abs foot-bg" viewBox="0 0 1200 472" preserveAspectRatio="none">
  <path d="M0 60 C200 10 400 60 600 40 C800 20 1000 0 1200 30 L1200 472 L0 472Z" fill="#7fd3cf"/>
  <path d="M0 110 C220 60 420 100 640 80 C860 60 1020 50 1200 70 L1200 472 L0 472Z" fill="#4dbdb9"/>
</svg>

<!-- contact -->
<div class="abs contact-card">
  <div class="abs form">
    <h2>CONTACT US</h2>
    <div class="fields">
      <div class="field">FIRST NAME*</div><div class="field">LAST NAME*</div>
      <div class="field">E-MAIL*</div><div class="field">PHONE*</div>
      <div class="field wide">MESSAGE</div>
    </div>
    <div class="send">SEND NOW</div>
  </div>
  <div class="abs details">
    <h2>CONTACT DETAILS</h2>
    <div class="d-row">
      <svg viewBox="0 0 30 30"><path d="M15 2C9 2 5 6.5 5 12C5 19 15 28 15 28S25 19 25 12C25 6.5 21 2 15 2Z" fill="#fff"/><circle cx="15" cy="12" r="4" fill="#1e7a78"/></svg>
      <span>4820 Harlow Ridge Drive, Suite 210<br>Westbrook, ST 00000</span>
    </div>
    <div class="d-row big">
      <svg viewBox="0 0 30 30"><circle cx="15" cy="15" r="14" fill="#fff"/><path d="M10 8L13 8L14 12L12 13.5C13 16 14 17 16.5 18L18 16L22 17L22 20C22 21 21 22 20 22C14 22 8 16 8 10C8 9 9 8 10 8Z" fill="#1e7a78"/></svg>
      <span>(555) 010-4471</span>
    </div>
    <div class="d-row">
      <svg viewBox="0 0 30 30"><circle cx="15" cy="15" r="14" fill="#fff"/><rect x="8" y="10" width="14" height="10" fill="#1e7a78"/><path d="M8 10L15 16L22 10" stroke="#fff" stroke-width="1.4" fill="none"/></svg>
      <span>hello@k7mc.example</span>
    </div>
    <div class="socials">
      <span><i></i>Updates</span><span><i></i>Newsfeed</span><span><i></i>Network</span>
    </div>
  </div>
</div>

<h2 class="abs foot-title">The K7<br>Momentum Collective™</h2>
<div class="abs foot-links">
  <p><b>Funding:</b> Venture Capital &nbsp;|&nbsp; Angel &nbsp;|&nbsp; Private Equity</p>
  <p><b>Other Sources:</b> Grants (Federal Agencies) &nbsp;|&nbsp; Philanthropic &nbsp;|&nbsp; Industry &nbsp;|&nbsp; Institutional &nbsp;|&nbsp; Loans</p>
</div>
<div class="abs foot-line"></div>
<p class="abs copy">© 2023 THE K7 MOMENTUM COLLECTIVE - ALL RIGHTS RESERVED</p>

</body>
</html>
```